Paper Lantern Design

Query PixelTent: THE PAPER LANTERN LEDGER
(commercial fiction, 85,000 words)

AUTHOR: Peter L. Hoskins [pen name] Author: Owen Carl Fenwick
Tamsin Ogilvy

Mass shooter, quadroon Ross Pemberley, schools reporter Lorraine Dawkins. Jewish commodity trader, Ari Lefkowitz, schools his trading partner, Neil Foster, on how it feels to be a minority. Pemberley’s shooting lands Ari in a coma, and they all school each other. How did they get so ignorant? And about what? Trading, i.e., capitalism. Politics, i.e., corruption. Killing, i.e., war. The stuff you only say in public, never with a friend of another ethnicity, i.e., racism. Therefore, the topic of this novel is allodoxaphobia. [stay with me]

How many gears does an Italian tank have? It’s got nineteen in reverse and one in forward in case the enemy attacks from the rear. If ethnic comedy is offensive, you might have caught allodoxaphobia.

Allodoxaphobia? A plague spreads unseen through America. It’s faced by a financial wizard [Jew boy], his partner [Whitey], and an African-American news lady. Three subcultures face allodoxaphobia—fear of conflicting opinions.

Lorraine Dawkins is sent with Frank “Mule” Kessler to cover a mass shooting in the Jewish suburb of Highland Park. KQT news gets her to take commodity trader, Neil Foster, to interview the quadroon shooter, Ross Pemberley, who justifies himself with brutal, woke truth that forces Lorraine to drop every racial inhibition and engage the Whitey with a variety of inappropriate interracial topics. Neil’s Jewish trading partner, Ari Lefkowitz, cannot be interviewed due to his coma.

Shooter, Pemberley, opens the door to the issues—war, capitalism, corruption, and race. All the issues climax at Ari’s memorial and Shiva.

Neil and Lorraine eventually turn romantic and the tension of the issues builds. Ross is shown to be a troubled shooter but not the killer. Ari’s brother has the fake art, “Dusk over Carmel,” and the KQT mole, a buxom beauty, uncovers corruption in the Lakeshore Watch.

QUALIFICATION? Fenwick’s childhood gets the blame—the Jim Crow South and the bazaars of Kabul, Afghanistan. Fenwick drove a bus on the Southside of Chicago, listened to innocent criminals for half a decade as a jail guard, then spent his careen trading in the pits of the Harvest Exchange. Hot tip from the floor: THE CROWD IS ALWAYS WRONG. It took Fenwick a couple of years to understand the meme, and a couple decades to resolve the themes of this novel.

WRITINGS His memoir, Ashes on the Ledger, was published by Brightwater, and he wrote Voice of the Mangroves, the memoir of an Amazon shaman. (both have sold about 40,000) He’s a member of Leon Tabbert’s Pit Oracle series.

COMPARABLES: (You’ll know this better than I)
Pelham’s Tobias Reedle for its emotional connections [and maybe racial language]
Voronkin’s Sisters Belovskaya, The spiritual themes are not as overt as Voronkin’s, but the undercurrent is audible for those with “ears to hear.”
Walter Quince's 2061 is more political and graphic. Nevertheless, child rape is graphic
Hartley, “A Harvest Ballad”
Samuel Branford’s, Edge of Silence
Maddox’s, “King of the Gulls,”

Best regards,
Owen Fenwick
https://owenfenwickpages.example/

African American, Jewish, manorities, academics, home schoolers

SIZE -- approx 9 X 6

• you can choose this
• I've sent many pictures and descriptions of the novel
• foul or off color pics

```html
<!DOCTYPE html>
<html lang="en">
<head>
<meta charset="utf-8">
<title>The Paper Lantern Ledger — Cover</title>
<link rel="stylesheet" href="https://fonts.googleapis.com/css2?family=Merriweather:wght@400;700;900&display=swap">
<style>
  :root {
    --backdrop: #e6e6e4;
    --paper: #efebdf;
    --ink: #141414;
    --ink-soft: #262626;
    --accent-red: #b3141b;
    --navy: #1f2f52;
    --steel: #5d6675;
    --slate: #9aa0aa;
    --brick: #8c1f24;
  }
  * { box-sizing: border-box; margin: 0; padding: 0; }
  html, body {
    width: 1194px;
    height: 1200px;
    overflow: hidden;
    background: var(--backdrop);
  }
  .stage {
    width: 1194px;
    height: 1200px;
    display: flex;
    align-items: center;
    justify-content: center;
  }
  .book-cover {
    position: relative;
    width: 720px;
    height: 1080px;
    background: var(--paper);
    overflow: hidden;
    box-shadow: 0 14px 34px rgba(0,0,0,0.16);
  }
  .cover-art {
    position: absolute;
    inset: 0;
    background:
      radial-gradient(ellipse 46% 22% at 50% 32%, var(--paper) 0%, rgba(239,235,223,0.9) 55%, rgba(239,235,223,0) 100%),
      radial-gradient(ellipse 34% 16% at 70% 85%, var(--paper) 0%, rgba(239,235,223,0.85) 55%, rgba(239,235,223,0) 100%),
      radial-gradient(ellipse 30% 26% at 68% 58%, rgba(140,31,36,0.75) 0%, rgba(140,31,36,0.35) 50%, rgba(140,31,36,0) 100%),
      radial-gradient(ellipse 30% 26% at 30% 66%, rgba(31,47,82,0.8) 0%, rgba(31,47,82,0.35) 50%, rgba(31,47,82,0) 100%),
      radial-gradient(ellipse 24% 12% at 30% 54%, rgba(80,22,26,0.75) 0%, rgba(80,22,26,0) 100%),
      radial-gradient(ellipse 40% 22% at 12% 100%, rgba(140,31,36,0.7) 0%, rgba(140,31,36,0) 100%),
      radial-gradient(ellipse 40% 24% at 92% 100%, rgba(31,47,82,0.85) 0%, rgba(31,47,82,0) 100%),
      radial-gradient(ellipse 30% 20% at 0% 8%, rgba(93,102,117,0.8) 0%, rgba(93,102,117,0) 100%),
      radial-gradient(ellipse 30% 20% at 100% 8%, rgba(31,47,82,0.7) 0%, rgba(31,47,82,0) 100%),
      linear-gradient(180deg, #9aa0aa 0%, #d2d1cb 16%, #ebe7db 34%, #c9c6c0 52%, #b7b9c2 70%, #d9d6cc 84%, #6e4a55 100%);
  }
  .cover-text {
    position: absolute;
    inset: 0;
    text-align: center;
    font-family: 'Merriweather', Georgia, serif;
    color: var(--ink);
  }
  .title {
    position: absolute;
    top: 215px;
    left: 0;
    right: 0;
    font-weight: 900;
    font-size: 56px;
    line-height: 1.0;
    letter-spacing: -0.5px;
  }
  .title-line { display: block; }
  .tagline {
    position: absolute;
    top: 400px;
    left: 60px;
    right: 60px;
    font-weight: 700;
    font-size: 20px;
    line-height: 1.3;
    color: var(--ink-soft);
  }
  .series {
    position: absolute;
    top: 462px;
    left: 0;
    right: 0;
    font-weight: 900;
    font-size: 28px;
    color: var(--accent-red);
  }
  .authors {
    position: absolute;
    top: 865px;
    left: 330px;
    right: 40px;
    font-weight: 900;
    font-size: 31px;
    line-height: 1.12;
  }
  .authors .joiner {
    display: block;
    font-size: 19px;
    font-weight: 700;
  }
</style>
</head>
<body>
  <main class="stage">
    <section class="book-cover">
      <div class="cover-art" role="img" aria-label="Fractured cubist illustration in navy, red and grey: a stock ticker board, a trader in a cap looking down, a woman and a man in profile, and a rifle, under shattered glass lines"></div>
      <div class="cover-text">
        <h1 class="title">
          <span class="title-line">The</span>
          <span class="title-line">Paper</span>
          <span class="title-line">Lantern Ledger</span>
        </h1>
        <p class="tagline">A brave, unflinching darkly funny novel<br>that dares to name what we pretend not to see</p>
        <p class="series">pit oracle journal</p>
        <p class="authors">
          Tamsin Ogilvy
          <span class="joiner">and</span>
          Peter Hoskins
        </p>
      </div>
    </section>
  </main>
</body>
</html>
```